Design Footer or Header for Pizza Restaurant Menu

-Design a footer or header using our logo and contact information.
-The menu items in the middle should be exactly as shown in the .psd examples.
-2 Pages (both should have the same design of Footer or Header)
-Menu Items (Document Link)
https://sheets.verbolt-docs.example/d/7QwXk2pLmN84rTzVbHc5yJd0eFsA91gUoKiRnP3tBMc6/edit?usp=sharing
Contact Information
1857 Marlowe Street, Harlow Ridge, NY 10473
555-318-4471
Crustello.com

```html
<!DOCTYPE html>
<html lang="en">
<head>
<meta charset="utf-8">
<title>Crustello Menu</title>
<link rel="stylesheet" href="https://fonts.googleapis.com/css2?family=Arimo:wght@400;700&family=Oswald:wght@200;300;500;700&display=swap">
<style>
:root{
  --red:#c0272d;
  --red-bright:#e3131b;
  --cream:#f7f5ec;
  --paper:#ffffff;
  --ink:#151515;
  --muted:#7a7a7a;
  --rule:#a9a9a9;
  --canvas:#ffffff;
}
*{box-sizing:border-box;margin:0;padding:0}
html,body{width:1200px;height:1200px;overflow:hidden;background:var(--canvas)}
body{position:relative;font-family:"Arimo",Arial,sans-serif;color:var(--ink)}
.page{position:absolute;top:145px;width:585px;height:910px;display:flex;flex-direction:column}
.page-main{left:10px;background:var(--cream)}
.page-pizza{left:605px;background:var(--paper)}

.masthead{background:var(--red);height:156px;display:flex;align-items:center;justify-content:space-between;padding:0 40px 0 34px;flex:none}
.brand{display:flex;align-items:center;gap:10px;color:#fff}
.brand-dot{width:22px;height:22px;border-radius:50%;background:#fff}
.brand-name{font-family:"Oswald",sans-serif;font-weight:300;font-size:50px;letter-spacing:1px;color:#fff}
.contact{font-family:"Oswald",sans-serif;font-weight:200;color:#fff;line-height:1.05;text-transform:uppercase}
.contact-site{font-size:34px}
.contact-phone{font-size:25px}

.menu-grid{display:grid;grid-template-columns:1fr 1fr;column-gap:12px;padding:0 10px}
.section-title{font-size:11.5px;color:var(--red-bright);text-align:center;text-transform:uppercase;letter-spacing:.3px}
.section-note{font-size:5.2px;color:var(--red-bright);text-align:center;text-transform:uppercase;margin-top:1px}
.section-rule{height:2px;background:var(--rule);margin:4px 0 9px}
.item{margin-bottom:5px}
.item-line{display:flex;align-items:baseline;font-size:8.4px;text-transform:uppercase;white-space:nowrap}
.leader{flex:1;border-bottom:1px dotted #555;margin:0 1px}
.desc{font-size:5.6px;color:var(--muted);text-transform:uppercase;line-height:1.2;padding-left:1px}

.row-top{height:356px;padding-top:14px}
.row-bottom{height:332px;padding-top:0}

.feature-box{border:2px solid var(--red-bright);border-radius:4px;background:#fff;text-align:center;padding:4px 6px 5px;margin:10px 0 0}
.feature-title{font-family:"Oswald",sans-serif;font-weight:700;color:var(--red-bright);font-size:13px;letter-spacing:.3px}
.feature-sub{font-family:"Oswald",sans-serif;font-weight:300;font-size:6.6px;color:#444;margin:2px 0 4px}
.feature-prices{font-family:"Oswald",sans-serif;font-weight:500;font-size:11.5px;letter-spacing:1.2px;color:#333;line-height:1.45}
.feature-prices sup{font-size:6px}
.feature-note{font-family:"Oswald",sans-serif;font-weight:300;font-size:5.4px;color:#444}

.toppings{display:grid;grid-template-columns:1fr 1px 1fr;gap:12px;margin:22px 20px 0;text-align:center;font-size:5.6px;font-weight:700;text-transform:uppercase;line-height:1.4}
.toppings-head{color:var(--red-bright);font-size:6.6px;margin-bottom:3px}
.toppings-divider{background:var(--rule)}

.footer-band{margin-top:auto;background:var(--red);height:66px;display:flex;align-items:center;padding:0 20px 0 120px;gap:40px;flex:none}
.footer-brand{display:flex;align-items:center;gap:6px;color:#fff}
.footer-brand .brand-dot{width:10px;height:10px}
.footer-brand .brand-name{font-size:20px}
.footer-contact{font-family:"Oswald",sans-serif;color:#fff;text-transform:uppercase;line-height:1.05;white-space:nowrap}
.footer-address{font-weight:200;font-size:14px}
.footer-hours{font-weight:300;font-size:11.5px}
.footer-phone{font-weight:200;font-size:14px}

.pizza-grid{display:grid;grid-template-columns:318px 1fr;column-gap:18px;padding:10px 12px 0;flex:1}
.size{font-size:4.6px}
.pizza .item{margin-bottom:3px}
.pizza .desc{font-size:5.4px}
.plain-list .item-line{font-size:8px;margin-bottom:8.5px}
.dessert .item{margin-bottom:7px}
.dessert .item-line{font-size:7.6px}
.dessert .desc{font-size:7.2px;color:#444}
.page-pizza .footer-band{height:110px}
.page-pizza .masthead{height:160px}
</style>
</head>
<body>

<article class="page page-main">
  <header class="masthead">
    <div class="brand"><span class="brand-dot"></span><span class="brand-name">Crustello</span></div>
    <div class="contact"><div class="contact-site">Crustello.com</div><div class="contact-phone">555-318-4471</div></div>
  </header>

  <div class="menu-grid row-top">
    <section>
      <h2 class="section-title">Appetizers</h2>
      <div class="section-rule"></div>
      <div class="item"><div class="item-line">Homemade Mozzarella Sticks (5)<span class="leader"></span>$10.50</div><p class="desc">Smoked mozzarella chunky sticks coated in breadcrumbs served with spicy tomato sauce</p></div>
      <div class="item"><div class="item-line">Homemade Chicken Nuggets (6)<span class="leader"></span>$9.50</div><p class="desc">Real homemade chicken nuggets (local farm raised chicken) served w/ french fries</p></div>
      <div class="item"><div class="item-line">Roasted Chicken Wings (6) (12)<span class="leader"></span>$9.00/$16.00</div><p class="desc">Seasoned available in our homemade buffalo sauce, garlic &amp; romano cheese, hickory smoked BBQ, honey BBQ, cajun dry rub, sweet chili sauce</p></div>
      <div class="item"><div class="item-line">Polpette (Meatballs) (5)<span class="leader"></span>$10.50</div><p class="desc">Homemade baked meatballs in rich tomato sauce with whipped buffalo ricotta</p></div>
      <div class="item"><div class="item-line">Firecracker Calamari<span class="leader"></span>$14.00</div><p class="desc">Crispy fried calamari with cherry peppers served with lemon aioli and marinara (your chose of spicy &amp; not spicy)</p></div>
      <div class="item"><div class="item-line">Crocchette di Patate (5)<span class="leader"></span>$9.50</div><p class="desc">Homemade potato croquettes filled w/ smoked mozzarella</p></div>
      <div class="item"><div class="item-line">Arancini (5)<span class="leader"></span>$12.50</div><p class="desc">Sourdough crumbed rice balls with mixed wild mushrooms grana padano and gorgonzola emulsion</p></div>
      <div class="item"><div class="item-line">Charred Brussels Sprouts<span class="leader"></span>$10.50</div><p class="desc">Brussels sprouts with crispy parmesan flakes</p></div>
      <div class="item"><div class="item-line">Homemade Fries<span class="leader"></span>$8.50</div><p class="desc">House cut fries w/ your choice: classic, cajun spice or parmesan &amp; truffle</p></div>
      <div class="item"><div class="item-line">Garlic Bread with Cheese<span class="leader"></span>$6.50</div><p class="desc">Homemade garlic bread on fresh Bellaforno Italian bread w/ side of marinara</p></div>
    </section>

    <section>
      <h2 class="section-title">Panini or Wraps</h2>
      <p class="section-note">(Served with pickle &amp; fries)</p>
      <div class="section-rule"></div>
      <div class="item"><div class="item-line">Burrata, Pesto, Tomatoes<span class="leader"></span>$12.00</div><p class="desc">Tomatoes, basil pesto, burrata, arugula, olive oil, cracked salt and pepper, balsamic reduction</p></div>
      <div class="item"><div class="item-line">Kickin' Cauliflower<span class="leader"></span>$12.00</div><p class="desc">Crispy buffalo cauliflower, garlic sauteed kale, provolone, pickled jalapenos, garlic aioli</p></div>
      <div class="item"><div class="item-line">King Caesar<span class="leader"></span>$14.00</div><p class="desc">Cajun chicken, romain, parmesan, caesar dressing</p></div>
      <div class="item"><div class="item-line">Sca-More-Za Please!<span class="leader"></span>$14.00</div><p class="desc">Caramelized onions, olives, basil, Camporosso tomato, scamorza, evoo</p></div>
      <div class="item"><div class="item-line">The Sizzler<span class="leader"></span>$14.00</div><p class="desc">Chicken cutlet, bacon, fresh mozzarella, jalapenos, vodka sauce</p></div>
      <div class="item"><div class="item-line">Not Cluckin' Around<span class="leader"></span>$14.00</div><p class="desc">Grilled chicken, monterey jack, avocado, tomato, pesto aioli</p></div>
      <div class="item"><div class="item-line">Great Bambino<span class="leader"></span>$14.00</div><p class="desc">Grilled chicken, prosciutto, fresh mozzarella, tomatoes pesto aioli</p></div>
      <div class="feature-box">
        <div class="feature-title">PARMIGIANA &amp; MILANESE</div>
        <div class="feature-sub">Milanese Style: Baby Arugula, Red Onion, Tomato, Shaved Parmigiano, Aged Balsamic</div>
        <div class="feature-prices">CHICKEN $28<sup>.75</sup> • JUMBO SHRIMP $33<sup>.75</sup><br>EGGPLANT $28<sup>.75</sup></div>
        <div class="feature-note">Subsitute Vodka Sauce $5.25</div>
      </div>
    </section>
  </div>

  <div class="menu-grid row-bottom">
    <section>
      <h2 class="section-title">Salads</h2>
      <div class="section-rule"></div>
      <div class="item"><div class="item-line">The Market Bowl<span class="leader"></span>$15.00</div><p class="desc">Romaine, tomatoes, corn, chickpeas, cucumbers, red onions, beets, carrots, avocado, pumpkin seeds, gorgonzola, shallot vinaigrette</p></div>
      <div class="item"><div class="item-line">Sweet Greens<span class="leader"></span>$14.00</div><p class="desc">Arugula, apples, walnuts, goat cheese, onion, red wine vinaigrette</p></div>
      <div class="item"><div class="item-line">The Caesar<span class="leader"></span>$12.00</div><p class="desc">Romaine, garlic croutons, parmesan, caesar dressing</p></div>
      <div class="item"><div class="item-line">Huskers Harvest<span class="leader"></span>$14.00</div><p class="desc">Shaved kale, shaved brussels sprouts, rainbow quinoa, carrots, cucumbers, sunflower seeds, red onions, dried cranberries, avocado, champagne vinaigrette</p></div>
      <div class="item"><div class="item-line">Un-Feta-Getable Bowl<span class="leader"></span>$14.00</div><p class="desc">Romaine, cucumbers, tomatoes, onions, kalamata olives, feta, greek dressing</p></div>
      <div class="item"><div class="item-line">Go Green<span class="leader"></span>$14.00</div><p class="desc">Spring greens, fennel, celery, pears, toasted almonds, basil, shaved parmesan, cracked pepper, olive oil, citrus vinaigrette</p></div>
      <div class="item"><div class="item-line">Avo-Cobbo Bowl<span class="leader"></span>$14.00</div><p class="desc">Romaine, tomatoes, cucumbers, chopped egg, avocado, red onions, shallot vinaigrette</p></div>
      <div class="item"><div class="item-line">Midwest Foodie Bowl<span class="leader"></span>$14.00</div><p class="desc">Romaine, corn, beans, pico de gallo, jack, avocado, chipotle ranch</p></div>
      <div class="toppings">
        <div><div class="toppings-head">Toppings - $6.00</div>Grilled Chicken<br>Breaded Chicken Cutlet<br>Cajun Chicken</div>
        <div class="toppings-divider"></div>
        <div><div class="toppings-head">Toppings - $7.00</div>Grilled Shrimp<br>Cajun Shrimp<br>Salmon<br>Sliced Skirt Steak</div>
      </div>
    </section>

    <section>
      <h2 class="section-title">Entrees</h2>
      <div class="section-rule"></div>
      <div class="item"><div class="item-line">Spaghetti Pesto alla Pollo<span class="leader"></span>$19.50</div><p class="desc">Sauteed chicken breast, creamy basil pesto sauce &amp; parmesan</p></div>
      <div class="item"><div class="item-line">Pasta w/ Meatballs<span class="leader"></span>$16.00</div><p class="desc">Pasta w/ homemade meatballs &amp; marinara sauce</p></div>
      <div class="item"><div class="item-line">Eggplant Parmigiana<span class="leader"></span>$16.00</div><p class="desc">Nicely battered eggplant, marinara, mozzarella with side of spaghetti</p></div>
      <div class="item"><div class="item-line">Penne Vodka<span class="leader"></span>$16.00</div><p class="desc">Touch of cream, tomato sauce, splash of vodka</p></div>
      <div class="item"><div class="item-line">Chicken Franchaise<span class="leader"></span>$19.50</div><p class="desc">Lightly flour battered chicken breast sauteed in lemon white wine broth</p></div>
      <div class="item"><div class="item-line">Chicken Parmigiana<span class="leader"></span>$18.50</div><p class="desc">Breaded chicken cutlet, smokey tomato sauce, parmesan and mozzarella over spaghetti</p></div>
      <div class="item"><div class="item-line">Chicken Scarpariello<span class="leader"></span>$20.00</div><p class="desc">Chicken with italian sausage, olives, capers, mushrooms, and lightly spiced tomato sauce over honey garlic mashed potatoes</p></div>
      <div class="item"><div class="item-line">Classic Shrimp Scampi<span class="leader"></span>$21.50</div><p class="desc">Shrimp scampi with fresh arugula, diced tomatoes, splash of lemon</p></div>
      <div class="item"><div class="item-line">Lasagna<span class="leader"></span>$16.50</div><p class="desc">Our take on an italian classic</p></div>
      <div class="item"><div class="item-line">Roasted Faroe Island Salmon<span class="leader"></span>$25.50</div><p class="desc">Cherry tomatoes, capers, kalamata olives, marinara over sauteed veggies</p></div>
      <div class="item"><div class="item-line">Thinly Sliced Skirt Steak<span class="leader"></span>$25.50</div><p class="desc">Served with smokey slaw, crispy polenta, and chimichurri</p></div>
      <div class="item"><div class="item-line">32-Hour Slow Roasted Short Rib<span class="leader"></span>$25.50</div><p class="desc">Glazed cherry tomatoes with roasted potatoes and fresh rosemary</p></div>
    </section>
  </div>

  <footer class="footer-band">
    <div class="footer-brand"><span class="brand-dot"></span><span class="brand-name">Crustello</span></div>
    <div class="footer-contact">
      <div class="footer-address">1857 Marlowe Street Harlow Ridge, NY 10473</div>
      <div class="footer-hours">Monday - Sunday 11AM - 9PM</div>
      <div class="footer-phone">555-318-4471</div>
    </div>
  </footer>
</article>

<article class="page page-pizza">
  <header class="masthead">
    <div class="brand"><span class="brand-dot"></span><span class="brand-name">Crustello</span></div>
    <div class="contact"><div class="contact-site">Crustello.com</div><div class="contact-phone">555-318-4471</div></div>
  </header>

  <div class="pizza-grid">
    <section class="pizza">
      <h2 class="section-title">Pizza</h2>
      <div class="section-rule"></div>
      <div class="item"><div class="item-line">The Big Cheese<span class="leader"></span>$17.00<span class="size">LARGE</span>/14.00<span class="size">PER</span></div><p class="desc">Classic new york pizza, topped with tomato sauce and mozzarella</p></div>
      <div class="item"><div class="item-line">Hot Stuff<span class="leader"></span>$21.00<span class="size">LARGE</span>/15.00<span class="size">PER</span></div><p class="desc">Chicken cutlet marinated in hot sauce, topped with homemade ranch dressing drizzle</p></div>
      <div class="item"><div class="item-line">BBQ Special<span class="leader"></span>$21.00<span class="size">LARGE</span>/15.00<span class="size">PER</span></div><p class="desc">Chicken cutlet marinated in tangy barbeque sauce</p></div>
      <div class="item"><div class="item-line">Pizza Margherita<span class="leader"></span>$21.00<span class="size">LARGE</span>/15.00<span class="size">PER</span></div><p class="desc">Margherita style pizza, topped with san marzano tomatoes, basil, mozzarella and olive oil drizzle</p></div>
      <div class="item"><div class="item-line">Great White<span class="leader"></span>$21.00<span class="size">LARGE</span>/15.00<span class="size">PER</span></div><p class="desc">Battered eggplant coated in homemade tomato sauce, mozzarella, parmesan and ricotta</p></div>
      <div class="item"><div class="item-line">Eggplant Delight<span class="leader"></span>$21.00<span class="size">LARGE</span>/15.00<span class="size">PER</span></div><p class="desc">Classic new york pizza, topped with tomato sauce and mozzarella</p></div>
      <div class="item"><div class="item-line">Chicken Club<span class="leader"></span>$21.00<span class="size">LARGE</span>/15.00<span class="size">PER</span></div><p class="desc">Breaded chicken cutlet coated in homemade tomato sauce, mozzarella, parmesan and ricotta</p></div>
      <div class="item"><div class="item-line">Classic Chicken Francese<span class="leader"></span>$21.00<span class="size">LARGE</span>/15.00<span class="size">PER</span></div><p class="desc">Battered chicken breast sauteed in lemon white wine broth</p></div>
      <div class="item"><div class="item-line">Hot Links<span class="leader"></span>$22.00<span class="size">LARGE</span>/16.00<span class="size">PER</span></div><p class="desc">Crumbled hot sausage and vodka sauce</p></div>
      <div class="item"><div class="item-line">Ulti-Meat<span class="leader"></span>$22.00<span class="size">LARGE</span>/16.00<span class="size">PER</span></div><p class="desc">Mozzarella, pastrami, salami, meatballs, creamy ricotta, chives, hot sausage, basil, caramelized onions, hot peppers</p></div>
      <div class="item"><div class="item-line">The Prosciutto*<span class="leader"></span>$22.00<span class="size">LARGE</span>/16.00<span class="size">PER</span></div><p class="desc">Prosciutto di parma, arugula, fresh mozzarella</p></div>
      <div class="item"><div class="item-line">Get Em To The Greek!<span class="leader"></span>$22.00<span class="size">LARGE</span>/16.00<span class="size">PER</span></div><p class="desc">Red onions, tomatoes, aromatic oregano, greek olives, feta cheese</p></div>
      <div class="item"><div class="item-line">Veggie Supreme*<span class="leader"></span>$22.00<span class="size">LARGE</span>/16.00<span class="size">PER</span></div><p class="desc">Tomatoes, smoked mozzarella, seasonal vegetables, olives capers, evoo</p></div>
      <div class="item"><div class="item-line">Ricotta Be Kidding Me!<span class="leader"></span>$22.00<span class="size">LARGE</span>/16.00<span class="size">PER</span></div><p class="desc">Ricotta, roasted garlic, charred baby broccoli, fresh mozzarella</p></div>
      <div class="item"><div class="item-line">Lots of Shrooms*<span class="leader"></span>$22.00<span class="size">LARGE</span>/16.00<span class="size">PER</span></div><p class="desc">Fresh mozzarella, cream of mushrooms, mushrooms, arugula, truffle oil, parmesan</p></div>
      <div class="item"><div class="item-line">Pizza My Heart<span class="leader"></span>$22.00<span class="size">LARGE</span>/16.00<span class="size">PER</span></div><p class="desc">Zucchini squash, artichoke hearts, garlic, fresh basil, oil, shaved parmesan</p></div>
      <div class="item"><div class="item-line">Veggiemore*<span class="leader"></span>$22.00<span class="size">LARGE</span>/16.00<span class="size">PER</span></div><p class="desc">Eggplant, zucchini, roasted peppers, fresh mozzarella, san marzano tomato sauce</p></div>
      <div class="item"><div class="item-line">Shrimp Pancetta*<span class="leader"></span>$22.00<span class="size">LARGE</span>/16.00<span class="size">PER</span></div><p class="desc">Shrimp, pancetta, arugula, fresh mozzarella, shaved parmesan, balsamic reduction</p></div>
      <div class="item"><div class="item-line">Crust-Cilian<span class="leader"></span>$19.00<span class="size">LARGE</span></div><p class="desc">Traditional thick crust sicilian style topped with tomato sauce and mozzarella</p></div>
      <div class="item"><div class="item-line">Grandma Pie<span class="leader"></span>$23.00<span class="size">LARGE</span></div><p class="desc">Thin crust topped with marinated tomato, fresh mozzarella, basil and garlic</p></div>
      <div class="item"><div class="item-line">Drunken Grandma<span class="leader"></span>$23.00<span class="size">LARGE</span></div><p class="desc">Crispy grandma style, topped with vodka sauce, fresh mozzarella, romano and fresh basil</p></div>
    </section>

    <div>
      <section class="plain-list">
        <h2 class="section-title">Pizza Toppings</h2>
        <div class="section-rule"></div>
        <div class="item-line">The Big Cheese<span class="leader"></span>$4.50</div>
        <div class="item-line">Anchovies<span class="leader"></span>$4.50</div>
        <div class="item-line">Artichoke Hearts<span class="leader"></span>$4.50</div>
        <div class="item-line">Bacon<span class="leader"></span>$4.50</div>
        <div class="item-line">Black Olives<span class="leader"></span>$4.50</div>
        <div class="item-line">Broccoli<span class="leader"></span>$4.50</div>
        <div class="item-line">Egg Plant<span class="leader"></span>$4.50</div>
        <div class="item-line">Extra Cheese<span class="leader"></span>$4.50</div>
        <div class="item-line">Fresh Garlic<span class="leader"></span>$4.50</div>
        <div class="item-line">Fresh Mushrooms<span class="leader"></span>$4.50</div>
        <div class="item-line">Green Peppers<span class="leader"></span>$4.50</div>
        <div class="item-line">Hot Cherry Peppers<span class="leader"></span>$4.50</div>
      </section>

      <section class="dessert" style="margin-top:22px">
        <h2 class="section-title">Desserts</h2>
        <div class="section-rule"></div>
        <div class="item"><div class="item-line">Plain Cremavella Crepe<span class="leader"></span>$9.00</div></div>
        <div class="item"><div class="item-line">Banana +<span class="leader"></span>$4.50</div><p class="desc">Fire roasted marshmello &amp; cremavella</p></div>
        <div class="item"><div class="item-line">Strawberry +<span class="leader"></span>$4.50</div><p class="desc">Fire roasted marshmello &amp; cremavella</p></div>
        <div class="item"><div class="item-line">Strawberry +<span class="leader"></span>$4.50</div><p class="desc">Fire roasted marshmello &amp; cremavella</p></div>
        <div class="item"><div class="item-line">Banana + Strawberry +<span class="leader"></span>$4.50</div><p class="desc">Fire roasted marshmello &amp; cremavella</p></div>
        <div class="item"><div class="item-line">Wild Berries +<span class="leader"></span>$4.50</div><p class="desc">Fire roasted marshmello &amp; cremavella</p></div>
        <div class="item"><div class="item-line">Mixed Fruits +<span class="leader"></span>$4.50</div><p class="desc">Fire roasted marshmello &amp; cremavella</p></div>
        <div class="item"><div class="item-line">Peanut Butter + Banana +<span class="leader"></span>$4.50</div><p class="desc">Fire roasted marshmello &amp; cremavella</p></div>
        <div class="item"><div class="item-line">Cinnamon + Apple + Brown Sugar +<span class="leader"></span>$4.50</div><p class="desc">Fire roasted marshmello &amp; cremavella</p></div>
      </section>
    </div>
  </div>

  <footer class="footer-band">
    <div class="footer-brand"><span class="brand-dot"></span><span class="brand-name">Crustello</span></div>
    <div class="footer-contact">
      <div class="footer-address">1857 Marlowe Street Harlow Ridge, NY 10473</div>
      <div class="footer-hours">Monday - Sunday 11AM - 9PM</div>
      <div class="footer-phone">555-318-4471</div>
    </div>
  </footer>
</article>

</body>
</html>
```